Biker App Design
Zielgruppe
VolmaSen erstellt eine App für Biker mit der:
- Motorradfahrer andere Biker finden können um gemeinsam zu fahren
- Motorradfahrer ihre Strecke tracken können um Punkte zu sammeln
- Biker können mit diesen Punkten Ränge aufsteigen 'Masterbiker, Anfänger, GuruFahrer, etc.', es soll eine Art 'Erfahrungsleiste' angezeigt werden
- Diese Punkte können gegen Gutscheine/Wertsachen eingelöst werden
- Es gibt Nachrichten (Art Blogeinträge) genau zu diesen Themen
Aufgabenstellung
Modernes Design
Reduziert
Es werden folgende Screens benötigt:
Startbild
Start - Dateneintragen:
Um den Fahrer besser mit anderen Fahren zu verknüpfen muss er folgende informationen angeben:
- Welche Art Motorrad fährt er? Sport, Vintage, Cross
- Männlich/Weiblich/Divers
- Geburtsjahr
- PLZ des Heimatorts
- Nickname
Startscreen um andere Biker zu suchen und damit eine Tour zu starten
- Hier sollte ein 'Map' Bild mit einem Kreis für den Umkreis dargestellt werden + Pins mit Personenbilder , welche
Personen in der Nähe sind und auch fahren möchten
- Hier sollte stehen, wieviel Punkte er noch benötigt um den nächsten Gutschein freizuschalten
Screen zum Start des Trackens
Screen während dem Tracken mit Pause/Stop-Option
Screen mit einem Überblick der neuen Blogeinträge
Screen beim beenden des Trackens (Strecke speichern, Bild hinzufügen, Freunde informieren ich bin angekommen)
Screen Profilseite, Bild des Bikers + Bike + Erfahrungspunkte + gesammelte Errungenschaften z.B. 'Mit 3 Freunden mehr als 1000km gefahren'
Screen Bestenliste, anhand der Punkte
Es sollen Dateiformate verwendet werden, die gut wiederverwendet werden können. Es sollen sich Bausteine aus diesen Design wiederverwenden lassen können.

```html
<!DOCTYPE html>
<html lang="en">
<head>
<meta charset="utf-8">
<title>Biker App – Tracking Screen</title>
<link href="https://fonts.googleapis.com/css2?family=Exo+2:wght@400;600;700&display=swap" rel="stylesheet">
<style>
:root{
  --page:#e6e6e4;
  --screen:#2b2b2b;
  --bar:#222222;
  --band:#303030;
  --text:#ffffff;
  --muted:#5a5a5a;
  --green:#41c23a;
  --red:#e23333;
}
*{box-sizing:border-box;margin:0;padding:0}
html,body{width:1200px;height:801px;overflow:hidden}
body{background:var(--page);font-family:"Exo 2",sans-serif;color:var(--text);position:relative}
.screen{position:absolute;left:415px;top:20px;width:370px;height:761px;background:var(--screen);border-radius:18px;overflow:hidden;display:flex;flex-direction:column}
.status-bar{height:26px;background:var(--bar);display:flex;justify-content:flex-end;align-items:center;gap:6px;padding:0 12px;font-size:13px}
.app-bar{height:50px;background:var(--bar);display:flex;align-items:center;padding:0 14px;gap:18px;border-top:1px solid #1c1c1c}
.app-bar .spacer{flex:1}
.compass{position:relative;height:150px}
.compass svg{position:absolute;left:0;top:0}
.stats{position:relative;flex:1}
.stat{position:relative;height:82px}
.ghost{position:absolute;font-size:46px;font-weight:700;color:rgba(255,255,255,.045);white-space:nowrap;top:18px;left:70px}
.label{position:absolute;font-size:13px;font-weight:600}
.tag{position:absolute;height:40px;background:var(--green);font-size:12px;font-weight:600;padding:4px 10px}
.tag.left{left:0;width:140px;clip-path:polygon(0 0,100% 0,84% 100%,0 100%)}
.tag.right{right:0;width:110px;text-align:right;clip-path:polygon(16% 0,100% 0,100% 100%,0 100%)}
.value{position:absolute;font-size:36px;font-weight:700;letter-spacing:1px;line-height:1}
.controls{height:70px;display:flex;background:var(--bar)}
.btn-pause{flex:1;display:flex;align-items:center;justify-content:center;gap:10px;font-size:17px;font-weight:600}
.btn-stop{flex:1.1;background:var(--red);display:flex;align-items:center;justify-content:center;gap:10px;font-size:17px;font-weight:600;clip-path:polygon(10% 0,100% 0,100% 100%,0 100%)}
.bottom-nav{height:70px;background:var(--screen);display:flex;justify-content:space-around;align-items:center;border-top:1px solid #1c1c1c}
</style>
</head>
<body>
<main class="screen">
  <div class="status-bar">
    <svg width="46" height="12" viewBox="0 0 46 12" aria-hidden="true"><path d="M0 2h12L6 10z" fill="#fff"/><path d="M16 11L26 1v10z" fill="#fff"/><rect x="31" y="1" width="6" height="10" fill="#fff"/></svg>
    <span>12:30</span>
  </div>
  <header class="app-bar">
    <svg width="20" height="14" viewBox="0 0 20 14" aria-label="Menu"><path d="M0 1h20M0 7h20M0 13h20" stroke="var(--muted)" stroke-width="2"/></svg>
    <span class="spacer"></span>
    <svg width="20" height="20" viewBox="0 0 20 20" aria-label="Search"><circle cx="8" cy="8" r="6" stroke="var(--muted)" stroke-width="2" fill="none"/><path d="M12.5 12.5L18 18" stroke="var(--muted)" stroke-width="2"/></svg>
    <svg width="20" height="20" viewBox="0 0 20 20" aria-label="Notifications"><path d="M4 15V9a6 6 0 0112 0v6l2 2H2z M8 18h4" stroke="var(--muted)" stroke-width="2" fill="none"/></svg>
    <svg width="20" height="20" viewBox="0 0 20 20" aria-label="Settings"><circle cx="10" cy="10" r="3.5" stroke="var(--muted)" stroke-width="2" fill="none"/><circle cx="10" cy="10" r="7.5" stroke="var(--muted)" stroke-width="2" stroke-dasharray="3 2.9" fill="none"/></svg>
  </header>
  <section class="compass">
    <svg width="370" height="150" viewBox="0 0 370 150" aria-label="Compass heading 278 degrees">
      <path d="M20 150 Q185 20 350 150" stroke="#3a3a3a" stroke-width="2" fill="none"/>
      <text x="185" y="40" text-anchor="middle" fill="var(--red)" font-family="Exo 2, sans-serif" font-weight="700" font-size="18">N</text>
      <text x="40" y="110" fill="#555" font-family="Exo 2, sans-serif" font-size="13">W</text>
      <polygon points="180,62 200,80 192,96 170,92" fill="#fff"/>
      <text x="185" y="128" text-anchor="middle" fill="var(--green)" font-family="Exo 2, sans-serif" font-weight="600" font-size="15">278°</text>
    </svg>
  </section>
  <section class="stats">
    <div class="stat">
      <span class="label" style="right:14px;top:4px">Recording Time</span>
      <span class="tag left" style="top:30px">hh:mm:ss</span>
      <span class="value" style="left:96px;top:32px">00:59:34</span>
    </div>
    <div class="stat">
      <span class="ghost">Distance</span>
      <span class="tag right" style="top:2px">km</span>
      <span class="value" style="right:90px;top:6px">165.3</span>
      <span class="label" style="left:24px;top:56px">Distance</span>
    </div>
    <div class="stat">
      <span class="ghost">Avrage</span>
      <span class="label" style="right:14px;top:4px">Avrage speed</span>
      <span class="tag left" style="top:30px;width:110px">km/h</span>
      <span class="value" style="left:100px;top:32px">121.3</span>
    </div>
    <div class="stat">
      <span class="ghost">Altitude</span>
      <span class="tag right" style="top:2px">m</span>
      <span class="value" style="right:90px;top:6px">1720</span>
      <span class="label" style="left:24px;top:56px">Altitude</span>
    </div>
  </section>
  <div class="controls">
    <div class="btn-pause">
      <svg width="12" height="18" viewBox="0 0 12 18" aria-hidden="true"><path d="M2 1v16M10 1v16" stroke="#fff" stroke-width="2.5"/></svg>Pause
    </div>
    <div class="btn-stop">
      <svg width="20" height="20" viewBox="0 0 20 20" aria-hidden="true"><rect x="2" y="2" width="16" height="16" rx="3" stroke="#fff" stroke-width="2.5" fill="none"/></svg>Stop
    </div>
  </div>
  <nav class="bottom-nav">
    <svg width="24" height="22" viewBox="0 0 24 22" aria-label="Map"><path d="M1 4l7-3 8 3 7-3v17l-7 3-8-3-7 3z M8 1v17 M16 4v17" stroke="#4a4a4a" stroke-width="2" fill="none"/></svg>
    <svg width="20" height="24" viewBox="0 0 20 24" aria-label="Routes"><path d="M3 23V2h14l-3 5 3 5H3" stroke="#4a4a4a" stroke-width="2" fill="none"/></svg>
    <svg width="48" height="48" viewBox="0 0 48 48" aria-label="Recording"><circle cx="24" cy="24" r="21" stroke="var(--red)" stroke-width="2" fill="none"/><circle cx="24" cy="24" r="11" fill="#fff"/></svg>
    <svg width="24" height="24" viewBox="0 0 24 24" aria-label="Feed"><rect x="2" y="7" width="14" height="14" rx="3" stroke="#4a4a4a" stroke-width="2" fill="none"/><path d="M8 4h10a3 3 0 013 3v10" stroke="#4a4a4a" stroke-width="2" fill="none"/></svg>
    <svg width="22" height="24" viewBox="0 0 22 24" aria-label="Profile"><circle cx="11" cy="7" r="5" stroke="#4a4a4a" stroke-width="2" fill="none"/><path d="M1 23a10 9 0 0120 0" stroke="#4a4a4a" stroke-width="2" fill="none"/></svg>
  </nav>
</main>
</body>
</html>
```